Professionelles Design für Use Case Präsentationen im B2B-Bereich

Wir sind ein Schweizer Technologieunternehmen (Kalvor GmbH, www.kalvor.ch), das datenbasierte Simulationen, Optimierung und Entscheidungsunterstützung für Unternehmen in Logistik, Produktion und Verkehr anbietet.
Ziel dieses Projekts ist es, bestehende Use Cases in ein modernes, visuell ansprechendes Format zu bringen, das unsere Kompetenz und den Nutzen für Kunden klar kommuniziert. Die Zielgruppe sind Entscheidungsträger in mittleren bis großen Industrieunternehmen (Bereichsleiter, Projektleiter, Geschäftsleitung).
Was wir brauchen:
– Ein cleanes, professionelles Design (PowerPoint oder PDF-Layout), das sich gut für Präsentationen, Whitepaper oder als LinkedIn-Content eignet.
– Klare Struktur mit Infografiken, Icons, Diagrammen oder Visualisierungen.
– Integration unseres Logos, Farbschemas und ggf. unseres Slogans.
Stilrichtung:
– Modern, technisch fundiert, aber nicht überladen
– Klar, direkt, seriös
– Gerne mit einem visuellen roten Faden (z. B. durchgängige Icons oder Layout-Struktur)
Ein Beispieldokument (UseCase Transportkosten) mit Inhalte ist angefügt. Ziel ist eine wiederverwendbare Vorlage, die wir für verschiedene Kunden-Use-Cases adaptieren können.
- Roboto

```html
<!DOCTYPE html>
<html lang="de">
<head>
<meta charset="utf-8">
<title>Kalvor – Use Case Transportkosten</title>
<link href="https://fonts.googleapis.com/css2?family=Roboto:wght@400;500;700;900&display=swap" rel="stylesheet">
<style>
  :root {
    --canvas: #e0e0e0;
    --paper: #ffffff;
    --accent: #dad86d;
    --ink: #111111;
    --badge: #000000;
    --map-a: #c9dcb3;
    --map-b: #e9ecd9;
    --dash-a: #f4f4f4;
    --dash-b: #e3e3e3;
  }
  * { box-sizing: border-box; margin: 0; padding: 0; }
  html, body { width: 1067px; height: 1200px; overflow: hidden; }
  body { background: var(--canvas); font-family: "Roboto", sans-serif; color: var(--ink); position: relative; }

  .slide { position: absolute; left: 57px; width: 953px; height: 536px; background: var(--paper); overflow: hidden; }
  .slide--one { top: 37px; }
  .slide--two { top: 615px; }

  .band { position: absolute; left: 0; top: 0; width: 740px; height: 62px; background: var(--accent); border-bottom-right-radius: 48px; }
  .band-corner { position: absolute; left: 0; top: 61px; width: 110px; height: 110px; background: var(--accent); }
  .band-corner::after { content: ""; position: absolute; inset: 0; background: var(--paper); border-top-left-radius: 110px; }

  .band-mark { position: absolute; left: 24px; top: 13px; width: 35px; height: 35px; border-radius: 50%; border: 3px solid var(--paper); }
  .band-title { position: absolute; left: 81px; top: 14px; font-size: 28px; font-weight: 900; letter-spacing: -0.2px; }

  .brand { position: absolute; left: 765px; top: 14px; display: flex; align-items: center; gap: 8px; }
  .brand-dot { width: 36px; height: 36px; border-radius: 50%; background: var(--accent); }
  .brand-name { font-size: 27px; font-weight: 700; color: var(--ink); letter-spacing: 0.5px; }

  .headline { position: absolute; left: 0; right: 0; top: 76px; text-align: center; font-size: 21.5px; font-weight: 700; }

  .card { position: absolute; width: 298px; height: 165px; background: var(--accent); }
  .card--left { left: 134px; border-bottom-left-radius: 64px; }
  .card--right { left: 521px; border-bottom-right-radius: 64px; }
  .card--top { top: 132px; }
  .card--bottom { top: 320px; }

  .card-title { position: absolute; font-size: 19.5px; font-weight: 700; line-height: 1.25; }
  .card--left .card-title { left: 40px; top: 15px; }
  .card--right .card-title { left: 57px; top: 15px; }
  .card--bottom.card--left .card-title { top: 17px; }
  .card--bottom.card--right .card-title { top: 17px; }

  .card-text { position: absolute; font-size: 11.3px; line-height: 17px; }
  .card--left .card-text { right: 27px; top: 72px; text-align: right; width: 250px; }
  .card--right .card-text { left: 31px; top: 72px; width: 250px; }
  .card--bottom .card-text { top: 70px; }

  .icon { position: absolute; width: 58px; height: 58px; border-radius: 50%; background: var(--badge); display: flex; align-items: center; justify-content: center; }
  .icon::before { content: ""; position: absolute; inset: 5px; border-radius: 50%; border: 1px dotted var(--paper); }
  .icon svg { width: 28px; height: 28px; fill: none; stroke: var(--paper); stroke-width: 1.5; stroke-linecap: round; stroke-linejoin: round; }
  .icon--a { left: 383px; top: 131px; }
  .icon--b { left: 511px; top: 131px; }
  .icon--c { left: 383px; top: 319px; }
  .icon--d { left: 511px; top: 319px; }

  .footer { position: absolute; left: 24px; top: 505px; font-size: 12.2px; font-weight: 700; }
  .page-no { position: absolute; right: 0; top: 499px; width: 99px; height: 33px; background: var(--badge); color: var(--paper); border-radius: 17px 0 0 17px; font-size: 12px; font-weight: 700; display: flex; align-items: center; justify-content: center; }

  .visual { position: absolute; top: 121px; width: 410px; height: 349px; }
  .visual--map { left: 80px; background: linear-gradient(135deg, var(--map-b), var(--map-a) 55%, var(--map-b)); }
  .visual--dashboard { left: 514px; background: linear-gradient(180deg, var(--dash-a), var(--dash-b)); }
</style>
</head>
<body>

<section class="slide slide--one">
  <div class="band"></div>
  <div class="band-corner"></div>
  <div class="band-mark"></div>
  <h1 class="band-title">Was wäre, wenn…</h1>
  <div class="brand"><span class="brand-dot"></span><span class="brand-name">Kalvor</span></div>
  <h2 class="headline">…Sie neue Standorte mit echten Transportkosten vergleichen könnten?</h2>

  <article class="card card--left card--top">
    <h3 class="card-title">Ausgangslage &amp; Ziel</h3>
    <p class="card-text">Ein Handelsunternehmen prüfte mehrere neue Standorte. Dabei ging es um die Frage: Wie verändern sich die Transportkosten und die Kundenbelieferung bei einem Umzug?</p>
  </article>
  <div class="icon icon--a">
    <svg viewBox="0 0 24 24"><path d="M14 4c3-1.5 6-1 6-1s.5 3-1 6l-6 6-4-4z"/><circle cx="15.5" cy="8.5" r="1.5"/><path d="M9 11l-4 1 2-3h4M13 15l-1 4 3-2v-4M7 17l-3 3"/></svg>
  </div>

  <article class="card card--right card--top">
    <h3 class="card-title">Die Lösung –<br>Unsere Simulation</h3>
    <p class="card-text">Wir kombinierten Standortdaten, Kundenadressen und Liefermengen mit einem automatisierten Tourenplaner. So wurden die neuen Transportkosten und Fahrzeiten für alle Varianten berechnet und visualisiert.</p>
  </article>
  <div class="icon icon--b">
    <svg viewBox="0 0 24 24"><rect x="3" y="4" width="18" height="12" rx="1"/><path d="M9 20h6M12 16v4"/><circle cx="12" cy="10" r="3"/><path d="M12 6v1M12 13v1M8 10h1M15 10h1"/></svg>
  </div>

  <article class="card card--left card--bottom">
    <h3 class="card-title">Der konkrete Nutzen</h3>
    <p class="card-text">Vergleich der Standorte mit echten Touren<br>Transparente Berechnung der Transportkosten<br>Klare Entscheidungsgrundlage für Geschäftsleitung<br>Erste Resultate in weniger als 3 Wochen</p>
  </article>
  <div class="icon icon--c">
    <svg viewBox="0 0 24 24"><path d="M3 15h4l4 2h4a1.5 1.5 0 0 0 0-3h-3M7 19l5 1 8-4a1.5 1.5 0 0 0-2-2l-4 2"/><circle cx="14" cy="8" r="3.5"/><path d="M12.5 8l1 1 2-2"/></svg>
  </div>

  <article class="card card--right card--bottom">
    <h3 class="card-title">Kundenfeedback</h3>
    <p class="card-text">„Wir wussten genau, welcher Standort für unsere Kundenbelieferung am effizientesten ist – datenbasiert und nachvollziehbar.“</p>
  </article>
  <div class="icon icon--d">
    <svg viewBox="0 0 24 24"><path d="M7 21v-7h3l2-5a1.5 1.5 0 0 1 2 1v3h4a1.5 1.5 0 0 1 1.5 2l-1 5a1.5 1.5 0 0 1-1.5 1zM4 14h3v7H4z"/><path d="M6 4l.6 1.3 1.4.2-1 1 .2 1.4L6 7.2l-1.2.7.2-1.4-1-1 1.4-.2zM12 2l.6 1.3 1.4.2-1 1 .2 1.4L12 5.2l-1.2.7.2-1.4-1-1 1.4-.2zM18 4l.6 1.3 1.4.2-1 1 .2 1.4L18 7.2l-1.2.7.2-1.4-1-1 1.4-.2z"/></svg>
  </div>

  <p class="footer">Jetzt testen: Standortentscheidung absichern mit Simulation • +41 44 310 52 80 • info@kalvor.ch</p>
  <div class="page-no">Page No: 01</div>
</section>

<section class="slide slide--two">
  <div class="band"></div>
  <div class="band-corner"></div>
  <div class="band-mark"></div>
  <h1 class="band-title">Was wäre, wenn…</h1>
  <div class="brand"><span class="brand-dot"></span><span class="brand-name">Kalvor</span></div>
  <h2 class="headline">…Sie neue Standorte mit echten Transportkosten vergleichen könnten?</h2>

  <div class="visual visual--map" role="img" aria-label="Karte der Schweiz mit Lagerstandorten und farbigen Kundenstopps der simulierten Touren"></div>
  <div class="visual visual--dashboard" role="img" aria-label="Dashboard der Tourenplanung mit Kennzahlen, Tourenkarte, Detailtabelle und Diagrammen pro Lager und Fahrzeug"></div>

  <p class="footer">Jetzt testen: Standortentscheidung absichern mit Simulation • +41 44 310 52 80 • info@kalvor.ch</p>
  <div class="page-no">Page No: 02</div>
</section>

</body>
</html>
```